Bright Cradle, Accelerator for Healthcare Startups, Grand Opening

Bright Cradle is an accelerator for healthcare startup businesses located in North Chicago, Illinois, USA. On July 16th, 4:30 - 6:30 pm, we are having a Grand Opening of our new location, which is at 2460 Walloway, North Chicago, IL. There will be many local dignitaries in attendance, but most importantly we will be unveiling the healthcare startup businesses that will be in our next cohort. We also have four sponsors, logos attached. Here's our website: http://brightcradle-example.ventures/

Target Market(s)

Investors, Healthcare Professionals, Politicians, Dignitaries

Industry/Entity Type

Healthcare

Requirements
Must have
• Logo, Date, Time, Location, Sponsors.
Nice to have
• Extremely elegant, professional design.
Should not have
• This is NOT and opening for retail. This is very professional.

```html
<!DOCTYPE html>
<html lang="en">
<head>
<meta charset="utf-8">
<title>Bright Cradle Grand Opening Invitation</title>
<link rel="stylesheet" href="https://fonts.googleapis.com/css2?family=Pinyon+Script&display=swap">
<style>
  :root {
    --tile: #e4e4e4;
    --tile-light: #f0f0f0;
    --ink: #1a1a1a;
    --brown: #8a4536;
    --white: #ffffff;
    --frame: #3a3a3a;
  }
  * { margin: 0; padding: 0; box-sizing: border-box; }
  html, body { width: 1200px; height: 780px; overflow: hidden; background: var(--white); }
  .invitation {
    position: relative;
    width: 1200px;
    height: 780px;
    overflow: hidden;
    font-family: "Pinyon Script", cursive;
  }
  .tile-backdrop {
    position: absolute;
    inset: 0;
    background: radial-gradient(circle at 50% 50%, var(--tile-light), var(--tile));
  }
  .frame {
    position: absolute;
    inset: 5px 6px 6px 8px;
    border: 1.5px solid var(--frame);
  }
  .line { position: absolute; white-space: nowrap; line-height: 1; }
  .invite-line { left: 252px; top: 62px; font-size: 44px; color: var(--ink); }
  .unveil-line { left: 405px; top: 188px; font-size: 44px; color: var(--ink); }
  .brand-band {
    position: absolute;
    left: 150px; top: 238px;
    width: 755px; height: 100px;
    background: var(--white);
    display: flex; align-items: center; justify-content: center;
  }
  .brand-name { font-size: 86px; font-weight: 400; color: var(--ink); line-height: 1; padding-top: 8px; }
  .address-line { left: 145px; top: 354px; font-size: 33px; color: var(--brown); }
  .date-line { left: 335px; top: 440px; font-size: 52px; color: var(--brown); }
  .time-line { left: 380px; top: 528px; font-size: 42px; color: var(--brown); }
  .web-line { left: 212px; top: 606px; font-size: 44px; color: var(--brown); }

  .sponsor {
    position: absolute;
    display: flex; align-items: center; justify-content: center; gap: 8px;
    color: var(--brown); line-height: 1.1; text-align: center;
  }
  .sponsor .mark-circle { flex: none; width: 14px; height: 14px; border-radius: 50%; background: var(--brown); }
  .sponsor-grill { left: 70px; top: 648px; width: 116px; height: 126px; background: var(--white); font-size: 26px; padding: 8px; }
  .sponsor-coffee { left: 300px; top: 710px; width: 250px; height: 40px; font-size: 20px; white-space: nowrap; }
  .sponsor-taproom { left: 612px; top: 690px; width: 210px; height: 50px; font-size: 26px; white-space: nowrap; }
  .sponsor-candy { left: 930px; top: 628px; width: 170px; height: 142px; background: var(--white); font-size: 28px; padding: 10px; }
</style>
</head>
<body>
<main class="invitation">
  <div class="tile-backdrop" role="img" aria-label="Embossed white pressed-tin ceiling tile pattern"></div>
  <div class="frame"></div>

  <p class="line invite-line">You Are Cordially Invited to</p>
  <p class="line unveil-line">Unveiling of</p>

  <div class="brand-band">
    <h1 class="brand-name">Bright Cradle</h1>
  </div>

  <p class="line address-line">North Chicago Illinois. U.S.A 2460 Walloway North Chicago, IL.</p>
  <p class="line date-line">July16th, 2015.</p>
  <p class="line time-line">4.30-6.30p.m</p>
  <p class="line web-line">www.brightcradle-example.ventures.com</p>

  <div class="sponsor sponsor-grill">Ember Grill</div>
  <div class="sponsor sponsor-coffee"><span class="mark-circle"></span>brewandbean-example.com</div>
  <div class="sponsor sponsor-taproom">Hopwell Taproom</div>
  <div class="sponsor sponsor-candy">Candy Orchard</div>
</main>
</body>
</html>
```